Business Card Design Project

Hi I am after a business card double sided 1 side to have the attached PDF on front on the back:

Tavi Rundell - Managing Director
Mobile: 0412 638 274
email: tavi@pruvo.com.au
web: www.pruvo.com.au

Industry/Entity Type

Business

Font styles to use
Sans Serif

Requirements
Must have
• I want a classy looking card
Nice to have
• I like lime green and black and white

```html
<!DOCTYPE html>
<html lang="en">
<head>
<meta charset="utf-8">
<title>Pruvo Lawns &amp; Gardens – Business Card</title>
<link rel="stylesheet" href="https://fonts.googleapis.com/css2?family=Questrial&display=swap">
<style>
  :root {
    --backdrop: #d1d2d4;
    --card: #ffffff;
    --ink: #000000;
    --lime: #2ab34b;
    --font: "Questrial", sans-serif;
  }
  * { margin: 0; padding: 0; box-sizing: border-box; }
  html, body {
    width: 1200px;
    height: 986px;
    overflow: hidden;
    background: var(--backdrop);
    font-family: var(--font);
    color: var(--ink);
  }
  .canvas { position: relative; width: 1200px; height: 986px; }

  .card {
    position: absolute;
    left: 90px; top: 185px;
    width: 1051px; height: 600px;
    background: var(--card);
    overflow: hidden;
  }
  .card__band {
    position: absolute;
    left: 0; top: 0;
    width: 188px; height: 100%;
    background: var(--ink);
  }
  .card__contact-tab {
    position: absolute;
    left: 153px; top: 393px;
    width: 420px; height: 194px;
    background: var(--card);
    border-radius: 28px 0 0 28px;
  }

  .identity { position: absolute; left: 219px; top: 62px; }
  .identity__name {
    font-size: 52px;
    font-weight: 400;
    line-height: 1;
    letter-spacing: -0.5px;
  }
  .identity__title {
    font-size: 31px;
    font-weight: 400;
    line-height: 1;
    margin-top: 8px;
  }

  .brand {
    position: absolute;
    left: 560px; top: 230px;
    width: 453px;
  }
  .brand__mark {
    display: block;
    width: 104px; height: 104px;
    background: var(--lime);
    border-radius: 12px;
  }
  .brand__name {
    margin-top: 14px;
    font-size: 29px;
    line-height: 1;
    white-space: nowrap;
    color: var(--ink);
  }

  .contact {
    position: absolute;
    left: 180px; top: 418px;
    list-style: none;
  }
  .contact__item {
    display: flex;
    align-items: center;
    height: 52px;
    font-size: 29px;
  }
  .contact__icon {
    width: 32px; height: 32px;
    margin-right: 19px;
    flex: none;
  }
</style>
</head>
<body>
<main class="canvas">
  <section class="card" aria-label="Business card">
    <div class="card__band"></div>
    <div class="card__contact-tab"></div>

    <header class="identity">
      <h1 class="identity__name">Tavi Rundell</h1>
      <p class="identity__title">Managing Director</p>
    </header>

    <div class="brand">
      <span class="brand__mark"></span>
      <p class="brand__name">Pruvo Lawns &amp; Gardens</p>
    </div>

    <ul class="contact">
      <li class="contact__item">
        <svg class="contact__icon" viewBox="0 0 32 32" aria-hidden="true">
          <rect x="13" y="1" width="2" height="6" fill="#000"/>
          <rect x="9" y="5" width="14" height="26" rx="2" fill="#000"/>
          <rect x="11" y="8" width="10" height="7" fill="#fff"/>
          <g fill="#fff">
            <rect x="11" y="18" width="2" height="2"/><rect x="15" y="18" width="2" height="2"/><rect x="19" y="18" width="2" height="2"/>
            <rect x="11" y="22" width="2" height="2"/><rect x="15" y="22" width="2" height="2"/><rect x="19" y="22" width="2" height="2"/>
            <rect x="11" y="26" width="2" height="2"/><rect x="15" y="26" width="2" height="2"/><rect x="19" y="26" width="2" height="2"/>
          </g>
        </svg>
        <span>0412 638 274</span>
      </li>
      <li class="contact__item">
        <svg class="contact__icon" viewBox="0 0 32 32" aria-hidden="true">
          <rect x="3" y="11" width="26" height="16" fill="#000"/>
          <polyline points="3,11 16,21 29,11" fill="none" stroke="#fff" stroke-width="1.5"/>
          <polyline points="3,27 12,18 M20,18 29,27" fill="none" stroke="#fff" stroke-width="1"/>
        </svg>
        <span>tavi@pruvo.com.au</span>
      </li>
      <li class="contact__item">
        <svg class="contact__icon" viewBox="0 0 32 32" aria-hidden="true">
          <circle cx="16" cy="17" r="12" fill="none" stroke="#000" stroke-width="2"/>
          <path d="M9 10c3 1 5 3 4 6s-3 3-2 6 1 4 0 5c-3-2-6-6-6-10 0-3 2-5 4-7z" fill="#000"/>
          <path d="M18 7c3 0 6 2 8 5-2 1-4 0-5 2s1 4 3 5-1 5-4 6c0-3-1-5-3-6s-2-4 0-6 2-3 1-6z" fill="#000"/>
        </svg>
        <span>www.pruvo.com.au</span>
      </li>
    </ul>
  </section>
</main>
</body>
</html>
```